Web Site Redesign

We operate a data centre facility specialing in colocation and Fibre optic connectivity (i.e. point to point fibre services and internet over fibre).

We have an existing site located at www.norvalex.example however this is very very tired and requires a redesign. We are looking for a fresh new design that will be appealing to potential customers.

The Company name is Norvale and the primary corporate colour is bright red with secondary colours of white, grey and black. Specific bright red can be seen in attached company logo.

Website needs to be modern, clean and professional representing our premium colocation and fibre provider branding.

Our company slogan is : safe. secure. reliable

We will provide feedback regardless of the quality of the design to ensure a better outcome for all parties.

Please feel free to contact us if you have any questions.

# The designer can use placeholder images or feel free to use any/all or none of the attached images
# The designer can use sample filler text

Target Market(s)

Technical IT Professionals as well C level executives (i.e. CEO's, CIO).

Industry/Entity Type

Internet

Requirements
Must have
• clean design
Nice to have
• A sidebar with two sections. 1 for current promo and 1 for "Let us call you back/contact you"
Should not have
• Clutter

```html
<!DOCTYPE html>
<html lang="en">
<head>
<meta charset="utf-8">
<title>Norvale — safe. secure. reliable.</title>
<link rel="stylesheet" href="https://fonts.googleapis.com/css2?family=Arimo:wght@400;700&display=swap">
<style>
:root{
  --brand-red:#e0282a;
  --tag-orange:#e8632a;
  --text-grey:#666666;
  --body-grey:#7a7a7a;
  --nav-grey:#555555;
  --rule:#d6d6d6;
  --hero-dark:#2e3a52;
  --hero-mid:#4b5a78;
  --white:#ffffff;
}
*{box-sizing:border-box;margin:0;padding:0}
html,body{width:1200px;height:1091px;overflow:hidden;background:var(--white);font-family:"Arimo",Arial,sans-serif}
.page{position:relative;width:1200px;height:1091px}
.top-bar{position:absolute;left:56px;top:0;width:1091px;height:8px;background:var(--brand-red)}
.brand{position:absolute;left:73px;top:118px;display:flex;align-items:center;gap:10px}
.brand-mark{width:18px;height:18px;background:var(--brand-red)}
.brand-name{font-size:30px;font-weight:700;color:var(--brand-red);line-height:1}
.header-tagline{position:absolute;left:916px;top:110px;font-size:20px;color:var(--tag-orange);word-spacing:4px}
.main-nav{position:absolute;left:56px;top:165px;width:1091px;height:44px;border:1px solid #dcdcdc;background:linear-gradient(#ffffff,#eef0f3)}
.main-nav a{position:absolute;top:11px;transform:translateX(-50%);font-size:16px;color:var(--nav-grey);text-decoration:none;white-space:nowrap}
.hero{position:absolute;left:57px;top:212px;width:1091px;height:364px;overflow:hidden}
.hero-photo{position:absolute;inset:0;background:linear-gradient(90deg,var(--hero-dark) 0%,var(--hero-mid) 48%,#8fa3bf 58%,#3a404c 68%,#1c1f26 100%)}
.hero-copy{position:absolute;left:40px;top:34px;width:570px;font-size:15px;line-height:28.4px;color:var(--white);text-align:justify}
.hero-button{position:absolute;left:41px;top:247px;width:194px;height:45px;border-radius:6px;background:linear-gradient(#ffffff,#dfe3e9);box-shadow:0 2px 4px rgba(0,0,0,.4);display:flex;align-items:center;padding-left:24px;gap:14px;font-size:18px;color:var(--brand-red);text-decoration:none}
.hero-band{position:absolute;left:0;bottom:0;width:100%;height:60px;background:rgba(255,255,255,.15);display:flex;align-items:center;padding-left:58px;font-size:33px;color:var(--white);letter-spacing:1.5px;word-spacing:10px}
.welcome{position:absolute;left:82px;top:618px;width:666px}
.welcome h1{font-size:23px;font-weight:400;color:var(--text-grey);margin-left:2px;margin-bottom:14px}
.welcome p{font-size:12.5px;line-height:24px;letter-spacing:.3px;color:var(--body-grey);text-align:justify;margin-bottom:24px}
.services{position:absolute;left:779px;top:607px;width:337px;height:298px;border-radius:8px 8px 0 0;background:linear-gradient(#f4f4f4,#ffffff 40%);box-shadow:0 0 6px rgba(0,0,0,.12)}
.services h2{font-size:24px;font-weight:400;color:var(--brand-red);padding:8px 0 0 19px;height:42px;border-bottom:1px solid var(--rule)}
.services ul{list-style:none;padding:2px 0 0 17px}
.services li{display:flex;align-items:center;gap:12px;height:26.2px;font-size:13px;color:var(--body-grey)}
.site-footer{position:absolute;left:55px;top:943px;width:1091px;height:82px;border-top:2px solid #d0d0d0;background:linear-gradient(#f2f2f2,#ffffff)}
.footer-nav{display:flex;justify-content:center;margin-top:12px;font-size:13px;color:#555;margin-left:-16px}
.footer-nav a{color:#555;text-decoration:none}
.footer-nav span{margin:0 19px}
.copyright{text-align:center;font-size:12px;color:#888;margin-top:16px;margin-left:-14px}
</style>
</head>
<body>
<div class="page">
  <div class="top-bar"></div>

  <header>
    <div class="brand"><span class="brand-mark"></span><span class="brand-name">Norvale</span></div>
    <div class="header-tagline">safe. secure. reliable.</div>
  </header>

  <nav class="main-nav">
    <a style="left:75px">Home</a>
    <a style="left:185px">About Us</a>
    <a style="left:305px">Facilities</a>
    <a style="left:468px">Business Continuity</a>
    <a style="left:635px">Services</a>
    <a style="left:756px">Partners</a>
    <a style="left:878px">Webmail</a>
    <a style="left:1000px">Contact Us</a>
  </nav>

  <section class="hero">
    <div class="hero-photo" role="img" aria-label="Data centre corridor lined with server rack cabinets, blue-toned"></div>
    <p class="hero-copy">orem Ipsum is simply dummy text of the printing and typesetting industry. Lorem Ipsum has been the industry's standard dummy text ever since the 1500s, when an unknown printer took a galley of type and scrambled it to make a type specimen book. It has survived not only five centuries, but also the leap into electronic typesetting, remaining essentially unchanged. It was popularised in the 1960s with the release of Lettersheet sheets containing Lorem</p>
    <a class="hero-button">Learn more
      <svg width="22" height="16" viewBox="0 0 22 16"><path d="M2 2l6 6-6 6M11 2l6 6-6 6" fill="none" stroke="#e0282a" stroke-width="3"/></svg>
    </a>
    <div class="hero-band">safe. secure. reliable.</div>
  </section>

  <section class="welcome">
    <h1>Welcome to Norvale</h1>
    <p>A world class data centre in the safest place on Earth. With a centrally located data centre in the heart of the Harbour CBD Norvale is excellently positioned to assist with your critical IT requirements.The CBD facility features overlapping power grids, redundant power supplies and comprehensively maintained infrastructure, providing excellent levels of protection for your critical IT equipment. The State's newest and most technologically advanced data centre is also now open in Eastvale, a convenient 5.5 km's from the CBD providing a perfect location for either production sites, or DR infrastructure.</p>
    <p>From Government departments to large corporations to SME's, Norvale is the ideal company to assist with your colocation requirements. With warm racks already provisioned, you can begin using the data centre almost immediately.</p>
  </section>

  <aside class="services">
    <h2>Our Services</h2>
    <ul>
      <li><svg width="17" height="15" viewBox="0 0 17 15"><path d="M1 8l5 5L16 1" fill="none" stroke="#e0282a" stroke-width="3"/></svg>Co-location</li>
      <li><svg width="17" height="15" viewBox="0 0 17 15"><path d="M1 8l5 5L16 1" fill="none" stroke="#e0282a" stroke-width="3"/></svg>Fibre connectivity</li>
      <li><svg width="17" height="15" viewBox="0 0 17 15"><path d="M1 8l5 5L16 1" fill="none" stroke="#e0282a" stroke-width="3"/></svg>Web Hosting</li>
      <li><svg width="17" height="15" viewBox="0 0 17 15"><path d="M1 8l5 5L16 1" fill="none" stroke="#e0282a" stroke-width="3"/></svg>Remote offsite backups</li>
      <li><svg width="17" height="15" viewBox="0 0 17 15"><path d="M1 8l5 5L16 1" fill="none" stroke="#e0282a" stroke-width="3"/></svg>Managed and hosted software solutions</li>
      <li><svg width="17" height="15" viewBox="0 0 17 15"><path d="M1 8l5 5L16 1" fill="none" stroke="#e0282a" stroke-width="3"/></svg>Internet Connectivity via Fibre</li>
      <li><svg width="17" height="15" viewBox="0 0 17 15"><path d="M1 8l5 5L16 1" fill="none" stroke="#e0282a" stroke-width="3"/></svg>Business grade DSL (Both ADSL and SHDSL)</li>
      <li><svg width="17" height="15" viewBox="0 0 17 15"><path d="M1 8l5 5L16 1" fill="none" stroke="#e0282a" stroke-width="3"/></svg>Point to Point Licensed Microwave links</li>
    </ul>
  </aside>

  <footer class="site-footer">
    <nav class="footer-nav">
      <a>Home</a><span>|</span><a>About Us</a><span>|</span><a>Facilities</a><span>|</span><a>Business Continuity</a><span>|</span><a>Services</a><span>|</span><a>Partners</a><span>|</span><a>Webmail</a><span>|</span><a>Contact Us</a>
    </nav>
    <p class="copyright">2010 Norvale All rights reserved</p>
  </footer>
</div>
</body>
</html>
```